VoltaRush Product Logo and Package

***Update*** Please you the text from the attached images on the product design.
Suggested Text:
Logo - VoltaRush
Title - Beta-hydroxybutyrates (BHB)Â Ketone Supplement
Beta-hydroxybutyrates (BHB)Â Ketone Supplement
Beta-hydroxybutyrates (BHB)Â Exogenous Ketones
Beta-hydroxybutyrates (BHB)Â Salts
Instant Ketones
3) Flavor - Orange Mango
4) Servings - 30 Servings 12g BHB Per Serving
5) Seals - Made in USA, FDA Certified Facility, GF (gluten Free), Dairy Free, Keto Friendly, Vegan Friendly, Non-GMO, Naturally Flavored, No Preservatives
6) Uses - Energy, Mental Clarity, Fat Loss, Muscle Strength, Appetite Suppression, Mood Management
7) Big Benefit - Formulated To Induce Rapid Ketosis.
Enjoy the benefits of Ketosis anytime!
50% More Servings Compared To Other Leading Brands!
I would like a logo and package designed for a supplement.
It is a powdered supplement that can be packaged in a plastic jar (8-16 oz) or a bag.
We will also be adding additional products to this line and would like the branding to scale.
The product is packaged in a 16 oz tub.
Product Title: Beta-hydroxybutyrates (BHB) Ketone Supplement
Brand Name: VoltaRush (I'd like the logo image to share the E)
Updates
Project Deadline Extended
Reason: I'd like to attract more designers and give them more time to submit briefs.
Target Market(s)
Health and Fitness Enthusiasts. Specifically those interested in a Ketogenic Lifestyle.
Industry/Entity Type
Health And Wellness
Requirements
Must have
- Modern, trendy, design.
- Bold colors and fonts.
- Professional but trendy.
- I would like to see Red and Black as the colors used.
Should not have
- Standard, corporate feel.
- Must be fun, engaging, and exciting.

```html
<!DOCTYPE html>
<html lang="en">
<head>
<meta charset="utf-8">
<title>VoltaRush — BHB Ketone Supplement pouches</title>
<link href="https://fonts.googleapis.com/css2?family=Fira+Sans:wght@300;400;600&display=swap" rel="stylesheet">
<style>
  :root {
    --backdrop: #b6b3ae;
    --pouch: #1c1a19;
    --pouch-edge: #121110;
    --cream: #e4e0d2;
    --band: #c9c4b0;
    --band-ink: #2a2624;
    --accent-red: #d3202e;
    --accent-crimson: #9e1420;
  }
  * { box-sizing: border-box; margin: 0; padding: 0; }
  html, body { width: 1200px; height: 900px; overflow: hidden; }
  body {
    background: var(--backdrop);
    font-family: "Fira Sans", sans-serif;
    position: relative;
  }
  .pouch {
    position: absolute;
    top: 210px;
    width: 348px;
    height: 614px;
    background: var(--pouch);
    border-radius: 2px 2px 10px 10px;
    box-shadow: inset 0 0 0 1px var(--pouch-edge);
  }
  .pouch--red { left: 244px; --accent: var(--accent-red); }
  .pouch--crimson { left: 646px; --accent: var(--accent-crimson); }
  .pouch__zip {
    position: absolute;
    top: 36px; left: 0; right: 0;
    height: 1px;
    background: rgba(255,255,255,0.08);
  }
  .pouch__tab {
    position: absolute;
    top: 0; right: 18px;
    width: 30px; height: 58px;
    background: var(--accent);
  }
  .brand {
    position: absolute;
    top: 112px; left: 0; right: 0;
    display: flex;
    align-items: center;
    justify-content: center;
    gap: 10px;
  }
  .brand__dot {
    width: 12px; height: 12px;
    border-radius: 50%;
    background: var(--accent);
  }
  .brand__name {
    font-weight: 600;
    font-size: 27px;
    color: var(--cream);
    letter-spacing: 0.2px;
  }
  .product-title {
    position: absolute;
    top: 282px; left: 0; right: 0;
    text-align: center;
    color: var(--cream);
    line-height: 1;
  }
  .product-title__light {
    display: block;
    font-weight: 300;
    font-size: 36px;
    letter-spacing: 2px;
  }
  .product-title__bold {
    display: block;
    font-weight: 600;
    font-size: 33px;
    letter-spacing: 1px;
    margin-top: 2px;
    color: var(--accent-red);
  }
  .pouch--crimson .product-title__bold { color: var(--cream); }
  .info-band {
    position: absolute;
    top: 376px; left: 0; right: 0;
    height: 72px;
    background: var(--band);
    display: flex;
    align-items: center;
    color: var(--band-ink);
  }
  .info-band__weight {
    width: 78px;
    padding-left: 24px;
    font-size: 13px;
    font-weight: 400;
    align-self: stretch;
    display: flex;
    align-items: center;
    border-right: 1px solid rgba(42,38,36,0.55);
    margin: 6px 0;
  }
  .info-band__claims {
    list-style: none;
    padding-left: 15px;
    font-size: 13px;
    font-weight: 300;
    line-height: 14px;
    letter-spacing: 0.6px;
  }
</style>
</head>
<body>
  <section class="pouch pouch--red">
    <div class="pouch__zip"></div>
    <div class="pouch__tab"></div>
    <div class="brand"><span class="brand__dot"></span><span class="brand__name">VoltaRush</span></div>
    <h1 class="product-title"><span class="product-title__light">BHB KETONE</span><span class="product-title__bold">SUPPLEMENT</span></h1>
    <div class="info-band">
      <div class="info-band__weight">16 oz</div>
      <ul class="info-band__claims">
        <li>orange mango</li>
        <li>30 servings · 12g BHB each</li>
        <li>RAPID KETOSIS</li>
      </ul>
    </div>
  </section>

  <section class="pouch pouch--crimson">
    <div class="pouch__zip"></div>
    <div class="pouch__tab"></div>
    <div class="brand"><span class="brand__dot"></span><span class="brand__name">VoltaRush</span></div>
    <h1 class="product-title"><span class="product-title__light">EXOGENOUS</span><span class="product-title__bold">KETONES</span></h1>
    <div class="info-band">
      <div class="info-band__weight">16 oz</div>
      <ul class="info-band__claims">
        <li>gluten &amp; dairy free</li>
        <li>keto &amp; vegan friendly</li>
        <li>MADE IN USA · NON-GMO</li>
      </ul>
    </div>
  </section>
</body>
</html>
```